New Business Card Design Project

We want a modern business card that catches the attention of other remodeling companies as well as homeowners. We would like it to be informative but still simple.

Target Market(s)

Residential and other Business's

Contact Information for Business Card

TrellBrix
Phone number is 5153927048
Address is
4817 SW 3rd Lane
Ardell, Kansas 60472
email is trellbrixco@quamlet.com

Requirements
Must have
• Our tagline
• Reliable | Dependable | Reasonable

```html
<!DOCTYPE html>
<html lang="en">
<head>
<meta charset="utf-8">
<title>TrellBrix Business Card</title>
<link rel="stylesheet" href="https://fonts.googleapis.com/css2?family=Oswald:wght@500;700&family=Roboto:wght@300;400&display=swap">
<style>
  :root {
    --page-bg: #e9e9ea;
    --card-bg: #3a393b;
    --brand-blue: #1f6fd8;
    --text-light: #e6e6e6;
    --divider: #2a5fb0;
    --emboss: #4a494c;
  }
  * { margin: 0; padding: 0; box-sizing: border-box; }
  html, body {
    width: 1200px; height: 801px; overflow: hidden;
    background: var(--page-bg);
  }
  .sheet {
    position: relative; width: 1200px; height: 801px;
    display: flex; align-items: center; justify-content: center; gap: 40px;
  }
  .card {
    position: relative; width: 540px; height: 309px;
    background: var(--card-bg);
    border-bottom: 4px solid var(--brand-blue);
    overflow: hidden;
  }
  .brand { position: absolute; }
  .brand-name {
    font-family: "Oswald", sans-serif; font-weight: 700;
    color: var(--brand-blue); letter-spacing: 2px; line-height: 1;
    text-transform: uppercase; white-space: nowrap;
  }
  .brand-tagline {
    font-family: "Oswald", sans-serif; font-weight: 500;
    color: var(--brand-blue); text-transform: uppercase;
    letter-spacing: 0.5px; white-space: nowrap;
  }
  /* Front */
  .card-front .brand { left: 40px; top: 128px; }
  .card-front .brand-name { font-size: 44px; }
  .card-front .brand-tagline { font-size: 11.5px; margin-top: 4px; }
  .divider {
    position: absolute; left: 282px; top: 60px; width: 1px; height: 180px;
    background: var(--divider);
  }
  .contact {
    position: absolute; left: 308px; top: 58px;
    font-family: "Roboto", sans-serif; font-weight: 300;
    color: var(--text-light); font-size: 14px; line-height: 21px;
    white-space: nowrap;
  }
  .contact-name { color: var(--brand-blue); font-size: 19px; font-weight: 400; line-height: 24px; }
  .contact-role { margin-bottom: 8px; }
  .contact-line { display: flex; align-items: center; gap: 8px; }
  .contact-line svg { width: 12px; height: 12px; flex: none; }
  .contact-address { margin-bottom: 6px; }
  .web-domain { color: var(--brand-blue); }
  /* Back */
  .emblem-area {
    position: absolute; left: 60px; top: 70px; width: 200px; height: 200px;
    border-radius: 50%;
    background: radial-gradient(circle at 40% 35%, #58575a, var(--emboss) 70%);
  }
  .card-back .brand { right: 34px; top: 176px; text-align: left; }
  .card-back .brand-name { font-size: 40px; }
  .card-back .brand-tagline { font-size: 10.5px; margin-top: 4px; }
</style>
</head>
<body>
<main class="sheet">
  <section class="card card-front" aria-label="Business card front">
    <div class="brand">
      <div class="brand-name">TrellBrix</div>
      <div class="brand-tagline">Reliable | Dependable | Reasonable</div>
    </div>
    <div class="divider"></div>
    <div class="contact">
      <div class="contact-name">Dalton Reeves</div>
      <div class="contact-role">Manager</div>
      <div class="contact-address">4817 SW 3rd Lane<br>Ardell, Kansas 60472</div>
      <div class="contact-line">
        <svg viewBox="0 0 12 12" aria-hidden="true"><path d="M2.5 1h2l1 3-1.3 1a6 6 0 0 0 2.8 2.8l1-1.3 3 1v2c0 .6-.4 1-1 1A10 10 0 0 1 1.5 2c0-.6.4-1 1-1z" fill="#1f6fd8"/></svg>
        <span>5153927048</span>
      </div>
      <div class="contact-line">
        <svg viewBox="0 0 12 12" aria-hidden="true"><rect x="1" y="2.5" width="10" height="7" fill="none" stroke="#1f6fd8" stroke-width="1.2"/><path d="M1 2.5l5 4 5-4" fill="none" stroke="#1f6fd8" stroke-width="1.2"/></svg>
        <span>trellbrixco@quamlet.com</span>
      </div>
      <div class="contact-line">
        <svg viewBox="0 0 12 12" aria-hidden="true"><circle cx="6" cy="6" r="5" fill="none" stroke="#1f6fd8" stroke-width="1.2"/><ellipse cx="6" cy="6" rx="2.2" ry="5" fill="none" stroke="#1f6fd8" stroke-width="1"/><path d="M1 6h10" stroke="#1f6fd8" stroke-width="1"/></svg>
        <span>www.<span class="web-domain">trellbrix</span>.com</span>
      </div>
    </div>
  </section>

  <section class="card card-back" aria-label="Business card back">
    <div class="emblem-area" role="img" aria-label="Embossed brand emblem area"></div>
    <div class="brand">
      <div class="brand-name">TrellBrix</div>
      <div class="brand-tagline">Reliable | Dependable | Reasonable</div>
    </div>
  </section>
</main>
</body>
</html>
```